Cleaning Service Company In need of Good Web presence.

The company is a cleaning service company which provides professional staff and service for cleaning. This is a project to build a site that is both solid and a strong recognition of our organization. It is supposed to show quality, cleanliness, professionalism. The use of images and art for imagery is all good just to have a site that is consistent and solid. There might be a chance to make stationary, logo and business cars if someone feels they can build a brand that is consistent. The image we are going for is clean solid and to stand out. Finally stationary should not be expensive to print.

Current logo is attached and can be used or can be made more creative.

Target Market(s)

Corporate and Government entities, that will feel that this company has a brand that sets it apart from the rest. The company is new so the modification of the logo will not be an issue if a more solid brand come out of this project. The idea is to have a clean consistent product that stands our from others in terms of website, stationary, etc

Industry/Entity Type

Cleaning Service

Contact Information for Business Card

P.O.Box 51947
Riffa
Kingdom of Bahrain

Logo Text

Brightmoor Facility Care

Number of Pages Required

4 page

Font styles to use
Sans Serif

Colors
abd036
cadf82
eaf2ce
9bcb3b

Requirements
Must have
• Green Color to be used in order to stick to the name. Also the creativity and boldness in an elegant manner.
Nice to have
• Arabic name of company
• برايتمور فاسيليتي كير ذ.م.م
• if cannot be put at least make a location should be chosen
• Also could be a bit of 3D given to the logo if it could stay elegent.
Should not have
• Should not show people cleaning.

```html
<!DOCTYPE html>
<html lang="en">
<head>
<meta charset="utf-8">
<title>Brightmoor Facility Care</title>
<link href="https://fonts.googleapis.com/css2?family=Open+Sans:ital,wght@0,400;0,600;0,700;1,600&display=swap" rel="stylesheet">
<style>
:root{
  --green:#9bcb3b;
  --green-bright:#abd036;
  --green-soft:#cadf82;
  --green-pale:#eaf2ce;
  --green-deep:#5e7f22;
  --ink:#2b2b2b;
  --text:#444;
  --frame:#e4e4e4;
  --white:#fff;
}
*{margin:0;padding:0;box-sizing:border-box}
html,body{width:1200px;height:2659px;overflow:hidden}
body{background:var(--frame);font-family:"Open Sans",Arial,sans-serif;color:var(--text);position:relative}
.page{position:absolute;left:14px;top:0;width:1172px;height:2641px;background:var(--white);overflow:hidden}
.abs{position:absolute}

/* header */
.contact-pill{left:635px;top:14px;width:508px;height:43px;background:var(--green);border-radius:0 0 8px 8px;display:flex;align-items:center;gap:26px;padding-left:28px;color:var(--white);font-size:13px;font-weight:600}
.contact-pill .item{display:flex;align-items:center;gap:8px}
.contact-pill .social{display:flex;gap:6px;margin-left:auto;margin-right:14px}
.contact-pill .social span{width:20px;height:20px;border:1.5px solid var(--white);border-radius:50%}
.top-line{left:0;top:0;width:1172px;height:4px;background:var(--green)}

.brand{display:flex;align-items:center;justify-content:center;text-align:center;border-radius:50%;background:var(--white);border:10px solid var(--green);color:var(--green-deep);font-weight:700;text-transform:uppercase;line-height:1.2;z-index:5;box-shadow:0 4px 10px rgba(0,0,0,.15)}
.brand-header{left:40px;top:44px;width:178px;height:178px;font-size:17px;padding:18px}

.nav{left:0;top:124px;width:1172px;height:37px;background:rgba(255,255,255,.92);z-index:3}
.nav ul{list-style:none;position:absolute;left:523px;top:0;display:flex;height:37px}
.nav li{display:flex;align-items:center;justify-content:center;font-size:14px;font-weight:700;color:var(--ink);text-transform:uppercase}
.nav li.active{background:var(--green);color:var(--white)}

.hero{left:0;top:124px;width:1172px;height:555px;background:linear-gradient(180deg,#e9eaec 0%,#f7f7f8 40%,#d9dbde 100%)}
.arrow{width:60px;height:46px;background:rgba(155,203,59,.85);display:flex;align-items:center;justify-content:center;top:397px}
.slide-dots{left:520px;top:653px;display:flex;gap:4px}
.slide-dots span{width:30px;height:5px;background:rgba(255,255,255,.8)}
.slide-dots span.on{background:var(--green)}

.tagline{left:0;top:679px;width:1172px;height:136px}
.tagline h1{position:absolute;left:0;top:30px;width:100%;text-align:center;color:var(--white);font-size:25px;font-weight:700;letter-spacing:.3px}

/* section headings */
.sec-head{left:0;width:1172px;display:flex;align-items:center;justify-content:center;gap:18px}
.sec-head .rule{width:100px;height:1px;background:#bbb}
.sec-head .dot{width:30px;height:30px;border-radius:50%;background:var(--green)}
.sec-head h2{font-size:24px;font-weight:700;color:var(--ink);text-transform:uppercase}
.sec-head h2 em{font-style:normal;color:var(--green)}

.about-text{left:58px;top:926px;width:1056px;text-align:center;font-size:14px;line-height:23px}
.btn{left:491px;top:1076px;width:192px;height:41px;background:var(--green);border-radius:6px;color:var(--white);font-weight:700;font-size:16px;display:flex;align-items:center;justify-content:center;box-shadow:0 6px 6px -3px rgba(0,0,0,.3)}

/* services */
.services{left:0;top:1175px;width:1172px;height:745px}
.services .sec-head h2{color:var(--white)}
.services .sec-head .rule{background:rgba(255,255,255,.5)}
.svc{width:340px;color:var(--white);font-size:14px;line-height:22px}
.svc h3{font-size:15px;font-weight:700;text-transform:uppercase;line-height:22px}
.brand-center{left:507px;top:1645px;width:184px;height:184px;font-size:17px;padding:22px;border-width:10px}

/* testimonials */
.quote{left:241px;top:2000px;width:692px;height:193px;border:1px solid #ccc;border-radius:6px;background:#fafafa;padding:20px 22px 0 58px;font-size:14px;line-height:22px;color:var(--text)}
.quote .mark{position:absolute;font-size:58px;font-weight:700;color:#666;line-height:1;font-family:Georgia,serif}
.quote-name{left:241px;top:2209px;font-size:16px;font-weight:600;font-style:italic;color:var(--ink)}
.t-dots{left:555px;top:2254px;display:flex;gap:4px}
.t-dots span{width:12px;height:12px;border-radius:50%;border:1.5px solid #777}
.t-dots span.on{background:var(--green);border-color:var(--green)}

/* footer */
.footer{left:0;top:2343px;width:1172px;height:270px;background:var(--green)}
.brand-footer{left:52px;top:2321px;width:178px;height:178px;font-size:17px;padding:18px}
.f-col{color:var(--white);font-size:12px;font-weight:700;line-height:20px;text-transform:uppercase}
.f-col h4{font-size:14px;font-weight:700;padding-bottom:6px;border-bottom:1px solid rgba(255,255,255,.8);margin-bottom:20px}
.f-line{display:flex;gap:10px;align-items:flex-start;margin-bottom:22px}
.field{border:1.5px solid var(--white);height:30px;margin-bottom:2px;padding:4px 8px;font-size:11px;font-weight:600;text-transform:none}
.submit{width:96px;height:28px;background:#222;color:var(--white);display:flex;align-items:center;justify-content:center;font-size:12px;font-weight:700;margin-top:6px}
.copyright{left:0;top:2613px;width:1172px;height:28px;background:var(--white);text-align:center;font-size:11px;font-weight:700;color:var(--ink);line-height:28px}
</style>
</head>
<body>
<div class="page">
  <div class="abs top-line"></div>

  <div class="abs hero" role="img" aria-label="Photograph of a bright, spotless white interior hall with tall windows"></div>
  <div class="abs arrow" style="left:0"><svg width="16" height="22" viewBox="0 0 16 22"><path d="M12 2 3 11l9 9" fill="none" stroke="#fff" stroke-width="3"/></svg></div>
  <div class="abs arrow" style="left:1112px"><svg width="16" height="22" viewBox="0 0 16 22"><path d="M4 2l9 9-9 9" fill="none" stroke="#fff" stroke-width="3"/></svg></div>
  <div class="abs slide-dots"><span class="on"></span><span></span><span></span></div>

  <nav class="abs nav">
    <ul>
      <li class="active" style="width:98px">Home</li>
      <li style="width:122px">About Us</li>
      <li style="width:130px">Our Services</li>
      <li style="width:176px">Testimonials</li>
      <li style="width:123px">Contact</li>
    </ul>
  </nav>

  <div class="abs contact-pill">
    <div class="item"><svg width="18" height="18" viewBox="0 0 18 18"><circle cx="9" cy="9" r="8.5" fill="none" stroke="#fff"/><path d="M6 4.5c-1 1-1 2.5 1 5s4 3.5 5 2.5l-1.5-1.8-1.2.6c-1-.6-2-1.6-2.4-2.6l.6-1.2z" fill="#fff"/></svg>123.456.7890</div>
    <div class="item"><svg width="18" height="18" viewBox="0 0 18 18"><circle cx="9" cy="9" r="8.5" fill="none" stroke="#fff"/><rect x="4.5" y="6" width="9" height="6" fill="none" stroke="#fff"/><path d="M4.5 6 9 9.5 13.5 6" fill="none" stroke="#fff"/></svg>info@brightmoorcare.com</div>
    <div class="social"><span></span><span></span><span></span></div>
  </div>

  <div class="abs brand brand-header">Brightmoor Facility Care</div>

  <div class="abs tagline">
    <svg class="abs" style="left:0;top:0" width="1172" height="136" viewBox="0 0 1172 136"><polygon points="0,0 1172,0 1172,96 586,136 0,96" fill="var(--green)"/></svg>
    <h1>THE TRUSTED NAME FOR PROFESSIONAL CLEANING SERVICES IN BAHRAIN</h1>
  </div>

  <div class="abs sec-head" style="top:864px"><span class="rule"></span><span class="dot"></span><h2>About <em>Us</em></h2><span class="rule"></span></div>
  <p class="abs about-text">Lorem ipsum dolor sit amet, consectetuer adipiscing elit, sed diam nonummy nibh euismod tincidunt ut laoreet dolore magna aliquam erat volutpat. Ut wisi enim ad minim veniam, quis nostrud exerci tation ullamcorper suscipit lobortis nisl ut aliquip ex ea commodo consequat. Duis autem vel eum iriure dolor in hendrerit in vulputate velit esse molestie consequat, vel illum dolore eu feugiat nulla facilisis at vero eros et accumsan et iusto odio dignissim qui blandit praesent luptatum zzril delenit augue duis dolore te feugait nulla facilisi. Nam liber tempor cum soluta nobis eleifend option congue nihil imperdiet doming id quod mazim placerat facer possim assum.</p>
  <div class="abs btn">Learn More</div>

  <section class="abs services">
    <svg class="abs" style="left:0;top:0" width="1172" height="745" viewBox="0 0 1172 745" role="img" aria-label="Photograph of a modern house with a garden at dusk, under a dark green tint">
      <defs><linearGradient id="svcBg" x1="0" y1="0" x2="0" y2="1"><stop offset="0" stop-color="#47533a"/><stop offset=".55" stop-color="#5a6642"/><stop offset="1" stop-color="#3f4b2c"/></linearGradient></defs>
      <polygon points="0,0 586,48 1172,0 1172,700 586,745 0,700" fill="url(#svcBg)"/>
    </svg>
    <div class="abs sec-head" style="top:97px"><span class="rule"></span><span class="dot"></span><h2>Our Services</h2><span class="rule"></span></div>

    <div class="abs svc" style="left:441px;top:180px;width:330px"><h3>Commercial</h3>Lorem ipsum dolor sit amet, consectetuer adipiscing elit, sed diam nonummy nibh euismod tincidunt ut laoreet dolore magna aliquam erat volutpat.</div>
    <div class="abs svc" style="left:35px;top:370px"><h3>Residential</h3>Lorem ipsum dolor sit amet, consectetuer adipiscing elit, sed diam nonummy nibh euismod tincidunt ut laoreet dolore magna aliquam erat volutpat.</div>
    <div class="abs svc" style="left:847px;top:370px"><h3>Holiday Homes</h3>Lorem ipsum dolor sit amet, consectetuer adipiscing elit, sed diam nonummy nibh euismod tincidunt ut laoreet dolore magna aliquam erat volutpat.</div>

    <svg class="abs" style="left:0;top:0" width="1172" height="745" viewBox="0 0 1172 745">
      <g fill="none" stroke="#fff" stroke-width="2">
        <path d="M418 453 Q585 370 752 453"/>
        <line x1="395" y1="438" x2="433" y2="481"/>
        <line x1="585" y1="393" x2="585" y2="420"/>
        <line x1="775" y1="438" x2="737" y2="481"/>
        <line x1="418" y1="453" x2="375" y2="500"/>
        <line x1="752" y1="453" x2="795" y2="500"/>
      </g>
      <g fill="var(--green-soft)" stroke="#fff" stroke-width="2">
        <circle cx="442" cy="477" r="8"/><circle cx="585" cy="430" r="8"/><circle cx="728" cy="477" r="8"/>
      </g>
      <g fill="#fff" stroke="var(--green-deep)" stroke-width="4">
        <circle cx="392" cy="413" r="44"/><circle cx="585" cy="349" r="44"/><circle cx="778" cy="413" r="44"/>
      </g>
      <g fill="var(--green)">
        <path d="M368 428 V410 L392 396 L416 410 V428 Z"/>
        <rect x="565" y="327" width="40" height="44"/>
        <path d="M756 430 V408 L778 390 L800 408 V430 Z"/>
      </g>
      <g fill="#fff">
        <rect x="376" y="414" width="6" height="6"/><rect x="389" y="414" width="6" height="6"/><rect x="402" y="414" width="6" height="6"/>
        <rect x="571" y="333" width="7" height="7"/><rect x="581" y="333" width="7" height="7"/><rect x="591" y="333" width="7" height="7"/>
        <rect x="571" y="346" width="7" height="7"/><rect x="581" y="346" width="7" height="7"/><rect x="591" y="346" width="7" height="7"/>
        <rect x="581" y="359" width="8" height="12"/>
        <rect x="773" y="416" width="10" height="14"/><rect x="762" y="412" width="7" height="7"/><rect x="788" y="412" width="7" height="7"/>
      </g>
    </svg>
  </section>
  <div class="abs brand brand-center">Brightmoor Facility Care</div>

  <div class="abs sec-head" style="top:1969px"><span class="rule"></span><span class="dot"></span><h2>Testimonials</h2><span class="rule"></span></div>
  <div class="abs quote">
    <span class="mark" style="left:14px;top:10px">&ldquo;</span>
    Lorem ipsum dolor sit amet, consectetuer adipiscing elit, sed diam nonummy nibh euismod tincidunt ut laoreet dolore magna aliquam erat volutpat. Ut wisi enim ad minim veniam, quis nostrud exercitation ullamcorper suscipit lobortis nisl ut aliquip ex ea commodo consequat. Duis autem vel eum iriure dolor in hendrerit in vulputate velit esse molestie consequat, vel illum dolore eu feugiat nulla facilisis at vero.
    <span class="mark" style="left:418px;top:118px">&rdquo;</span>
    <svg class="abs" style="left:30px;top:191px" width="26" height="16" viewBox="0 0 26 16"><path d="M0 0 L13 14 L26 0" fill="#fafafa" stroke="#ccc"/><rect x="1" y="0" width="24" height="2" fill="#fafafa"/></svg>
  </div>
  <div class="abs quote-name">Mara Ellison</div>
  <div class="abs t-dots"><span class="on"></span><span></span><span></span><span></span></div>

  <footer class="abs footer">
    <div class="abs f-col" style="left:307px;top:32px;width:160px">
      <h4>Quick Links</h4>
      <div>Home</div><div>About Us</div><div>Our Services</div><div>Testimonials</div><div>Contact Us</div>
    </div>
    <div class="abs f-col" style="left:495px;top:32px;width:200px">
      <h4>Contact</h4>
      <div class="f-line"><svg width="18" height="18" viewBox="0 0 18 18"><circle cx="9" cy="9" r="8.5" fill="none" stroke="#fff"/><path d="M9 4a3 3 0 0 0-3 3c0 2.5 3 6 3 6s3-3.5 3-6a3 3 0 0 0-3-3z" fill="#fff"/></svg><div>Brightmoor Facility Care W.L.L<br>123 Lorem Ipsum<br>Bahrain, UAE</div></div>
      <div class="f-line"><svg width="18" height="18" viewBox="0 0 18 18"><circle cx="9" cy="9" r="8.5" fill="none" stroke="#fff"/><path d="M6 4.5c-1 1-1 2.5 1 5s4 3.5 5 2.5l-1.5-1.8-1.2.6c-1-.6-2-1.6-2.4-2.6l.6-1.2z" fill="#fff"/></svg><div>123-456-7890</div></div>
      <div class="f-line"><svg width="18" height="18" viewBox="0 0 18 18"><circle cx="9" cy="9" r="8.5" fill="none" stroke="#fff"/><rect x="4.5" y="6" width="9" height="6" fill="none" stroke="#fff"/><path d="M4.5 6 9 9.5 13.5 6" fill="none" stroke="#fff"/></svg><div style="text-transform:lowercase">info@brightmoorcare.com</div></div>
    </div>
    <div class="abs f-col" style="left:776px;top:32px;width:282px">
      <h4>Send a Message</h4>
      <div class="field" style="width:282px">Name</div>
      <div class="field" style="width:282px">Email</div>
      <div class="field" style="width:282px;height:62px">Message</div>
      <div class="submit">SUBMIT</div>
    </div>
  </footer>
  <div class="abs brand brand-footer">Brightmoor Facility Care</div>

  <div class="abs copyright">COPYRIGHT &copy; 2017 BRIGHTMOOR FACILITY CARE W.L.L. ALL RIGHTS RESERVED.</div>
</div>
</body>
</html>
```